Sports Pre-Workout Supplement Company Needs a Package Design

We need a package design for new company located in Rockport, Maine called "PlumBlaze." We manufacture and distribute pre-workout supplements with beets as our primary ingredient.

We would like to see designs that use deep purple and green. The final design should communicate heart health and beneficial to endurance athletes (running, biking, swimming).

Industry/Entity Type

Health

Requirements
Must have
• The design must have the slogan, "The Healthy Option For Your Pre-Workout"

```html
<!DOCTYPE html>
<html lang="en">
<head>
<meta charset="utf-8">
<title>PlumBlaze Pre-Workout Label</title>
<link href="https://fonts.googleapis.com/css2?family=Cabin:wght@500&family=PT+Sans+Narrow:wght@700&display=swap" rel="stylesheet">
<style>
  :root {
    --bg: #f1f1f1;
    --green: #7dc242;
    --purple: #4a1c4f;
    --red: #c8161d;
    --beet-tone: #b42a2e;
    --white: #ffffff;
  }
  html, body {
    margin: 0;
    padding: 0;
    overflow: hidden;
  }
  .canvas {
    position: relative;
    width: 1200px;
    height: 1200px;
    overflow: hidden;
    background: radial-gradient(circle at 50% 45%, #ffffff 0%, var(--bg) 70%, #e4e4e4 100%);
  }
  .label {
    position: absolute;
    left: 318px;
    top: 402px;
    width: 588px;
    height: 402px;
    background: var(--green);
    overflow: hidden;
  }
  .label-purple {
    position: absolute;
    inset: 0;
  }
  .brand-heading {
    position: absolute;
    left: 16px;
    top: 56px;
    margin: 0;
    font-family: "Cabin", sans-serif;
    font-weight: 500;
    font-size: 92px;
    line-height: 1;
    letter-spacing: 0;
    color: var(--white);
  }
  .activity-icons {
    position: absolute;
    left: 22px;
    top: 182px;
    display: flex;
    gap: 14px;
  }
  .activity-icon {
    width: 40px;
    height: 40px;
    background: var(--red);
  }
  .slogan {
    position: absolute;
    left: 22px;
    top: 242px;
    margin: 0;
    font-family: "PT Sans Narrow", sans-serif;
    font-weight: 700;
    font-size: 31px;
    line-height: 35px;
    color: var(--white);
    text-transform: uppercase;
  }
  .beet-art {
    position: absolute;
    left: 204px;
    top: 160px;
    width: 262px;
    height: 218px;
    border-radius: 40px;
    background: radial-gradient(ellipse at 50% 55%, var(--beet-tone) 0%, rgba(180, 42, 46, 0.6) 55%, rgba(180, 42, 46, 0) 80%);
  }
  .net-weight {
    position: absolute;
    left: 470px;
    top: 346px;
    margin: 0;
    font-family: "Cabin", sans-serif;
    font-size: 12px;
    line-height: 14px;
    color: var(--white);
    text-align: right;
  }
  .net-weight strong {
    display: block;
    font-size: 15px;
  }
  .brand-lockup {
    position: absolute;
    left: 64px;
    top: 1096px;
    margin: 0;
    font-family: "Cabin", sans-serif;
    font-weight: 500;
    font-size: 74px;
    line-height: 1;
    letter-spacing: 1px;
    color: var(--red);
  }
</style>
</head>
<body>
  <div class="canvas">
    <section class="label">
      <svg class="label-purple" width="588" height="402" viewBox="0 0 588 402" aria-hidden="true">
        <path d="M246 0 Q140 201 210 402 L588 402 L588 0 Z" fill="var(--purple)"/>
      </svg>

      <h1 class="brand-heading">PLUMBLAZE</h1>

      <div class="activity-icons">
        <div class="activity-icon" role="img" aria-label="Running icon"></div>
        <div class="activity-icon" role="img" aria-label="Cycling icon"></div>
        <div class="activity-icon" role="img" aria-label="Swimming icon"></div>
      </div>

      <p class="slogan">The Healthy<br>Option<br>For Your<br>Pre-Workout</p>

      <div class="beet-art" role="img" aria-label="Illustration of two sliced beets with leaves"></div>

      <p class="net-weight">NET WT<strong>32oz</strong></p>
    </section>

    <p class="brand-lockup">PLUMBLAZE</p>
  </div>
</body>
</html>
```